Design for online reviews widget

Attached is a wireframe of a widget we need designing to display reviews on websites from multiple sources. We need this provided at 3 different sizes including full screen, contained (like the wireframe) and mobile.
You have completely free rein on the styling.
The only elements that should remain untouched are the blue stars (https://www.filquarry.net/s/8vtmwp2291zq4h/kv%20stars.ai?dl=0) and powered by logo at the bottom.
Ignore the menu at the top of the wireframe, this is just from the website the widget will be placed on.
Businesses

```html
<!DOCTYPE html>
<html lang="en">
<head>
<meta charset="utf-8">
<title>Reviews Widget</title>
<link rel="stylesheet" href="https://fonts.googleapis.com/css2?family=Lexend:wght@400;500;600;700&family=Arimo:wght@400;700&display=swap">
<style>
:root{
  --page:#e8fafd;
  --topbar:#b3ecfb;
  --card:#f3fcfe;
  --accent:#3bbfef;
  --ink:#111111;
  --meta:#4f9a1c;
  --star-gold:#f5c518;
  --brand:#1c5fb8;
  --white:#ffffff;
}
*{box-sizing:border-box;margin:0;padding:0}
html,body{width:1200px;height:955px;overflow:hidden;background:var(--page)}
body{position:relative;font-family:"Arimo",Arial,sans-serif;color:var(--ink)}
.topbar{position:absolute;left:251px;top:0;width:698px;height:6px;background:var(--topbar)}
.summary{position:absolute;left:480px;top:34px;width:240px;text-align:center}
.summary-stars{display:flex;justify-content:center;gap:5px}
.summary-text{font-family:"Lexend",sans-serif;font-size:12.5px;font-weight:500;margin-top:4px}
.filter{position:absolute;left:819px;top:69px;width:116px;height:20px;background:var(--white);border-radius:10px;font-size:10px;line-height:20px;padding-left:12px}
.filter svg{position:absolute;right:9px;top:7px}
.card{position:absolute;background:var(--card);border-radius:12px;border-bottom:5px solid var(--accent);padding:0 22px}
.card-ct{left:263px;top:133px;width:322px;height:296px;padding-top:29px}
.card-gg{left:614px;top:133px;width:322px;height:266px;padding-top:26px}
.card-yl{left:263px;top:464px;width:322px;height:260px;padding-top:27px}
.card-tp{left:614px;top:431px;width:322px;height:228px;padding-top:27px}
.badge-score{position:absolute;left:26px;top:-22px;width:46px;height:46px;border-radius:50%;background:#0e4f9e;border:3px solid var(--white);box-shadow:0 0 0 2px #0e4f9e}
.badge-stars{position:absolute;left:19px;top:-9px;width:90px;height:26px;background:var(--white);display:flex;align-items:center;justify-content:center;gap:1px}
.brand{display:flex;align-items:center;gap:5px;font-family:"Lexend",sans-serif;font-size:16px;font-weight:500;color:var(--brand);height:22px}
.brand-mark{width:12px;height:12px;background:var(--brand)}
.title{font-family:"Lexend",sans-serif;font-size:16.5px;font-weight:500;line-height:19px;margin-top:6px}
.body{font-size:9.6px;line-height:11.8px;margin-top:14px}
.card-ct .body{line-height:14.7px;margin-top:15px}
.scores{font-size:9.6px;font-weight:700;line-height:14.7px;margin-top:14px}
.service{font-size:9.6px;font-weight:700;margin-top:13px}
.meta{font-size:9.6px;color:var(--meta);margin-top:12px}
.load-more{position:absolute;left:526px;top:759px;width:149px;height:41px;border-radius:21px;background:var(--accent);color:var(--white);font-family:"Arimo",sans-serif;font-weight:700;font-size:16px;line-height:41px;text-align:center}
.powered{position:absolute;left:768px;top:849px;width:182px}
.powered-label{font-size:12px;text-align:center;padding-left:24px}
.powered-row{display:flex;align-items:center;gap:6px;margin-top:7px}
.powered-mark{width:40px;height:40px;border-radius:50%;background:linear-gradient(135deg,#f7d33b,#e84a8a,#3bbfef,#48c06a)}
.powered-name{font-family:"Lexend",sans-serif;font-weight:700;font-size:19px;color:#222}
</style>
</head>
<body>
<div class="topbar"></div>

<section class="summary">
  <div class="summary-stars">
    <svg width="33" height="33" viewBox="0 0 33 33"><circle cx="16.5" cy="16.5" r="16.5" fill="#3bbfef"/><path d="M16.5 6l3 7 7.5.6-5.7 5 1.8 7.4-6.6-4-6.6 4 1.8-7.4-5.7-5 7.5-.6z" fill="#fff"/></svg>
    <svg width="33" height="33" viewBox="0 0 33 33"><circle cx="16.5" cy="16.5" r="16.5" fill="#3bbfef"/><path d="M16.5 6l3 7 7.5.6-5.7 5 1.8 7.4-6.6-4-6.6 4 1.8-7.4-5.7-5 7.5-.6z" fill="#fff"/></svg>
    <svg width="33" height="33" viewBox="0 0 33 33"><circle cx="16.5" cy="16.5" r="16.5" fill="#3bbfef"/><path d="M16.5 6l3 7 7.5.6-5.7 5 1.8 7.4-6.6-4-6.6 4 1.8-7.4-5.7-5 7.5-.6z" fill="#fff"/></svg>
    <svg width="33" height="33" viewBox="0 0 33 33"><circle cx="16.5" cy="16.5" r="16.5" fill="#3bbfef"/><path d="M16.5 6l3 7 7.5.6-5.7 5 1.8 7.4-6.6-4-6.6 4 1.8-7.4-5.7-5 7.5-.6z" fill="#fff"/></svg>
    <svg width="33" height="33" viewBox="0 0 33 33"><circle cx="16.5" cy="16.5" r="16.5" fill="#3bbfef"/><path d="M16.5 6l3 7 7.5.6-5.7 5 1.8 7.4-6.6-4-6.6 4 1.8-7.4-5.7-5 7.5-.6z" fill="#fff"/></svg>
  </div>
  <p class="summary-text">Combined Review Score 4.3 out of 5</p>
</section>

<div class="filter">Filter Results
  <svg width="7" height="5" viewBox="0 0 7 5"><path d="M0 0h7L3.5 5z" fill="#3bbfef"/></svg>
</div>

<article class="card card-ct">
  <div class="badge-score"></div>
  <div class="brand">TradeVouch</div>
  <h2 class="title">Front door with windows each<br>side and side window</h2>
  <p class="body">This is the second time we have used meridian home Improvments , and the service is amazing! Daniel came round several times as we keep changing our minds and he was so helpful and gave us good advice, and the guys who do the fitting are efficient and tidy . I’ve got to say the end result is amazing and I have recommended to many of friends . Thanks Meridan</p>
  <p class="scores">Reliablity: 9.38 Courtesy: 10 Tidiness: 9.84<br>Workmanship: 10</p>
  <p class="meta">Verified 28th September 2021 | Located in Ashford</p>
</article>

<article class="card card-gg">
  <div class="badge-stars">
    <svg width="85" height="16" viewBox="0 0 85 16"><g fill="#f5a623"><path id="s" d="M8 0l2.4 5 5.4.6-4 3.7 1.1 5.4L8 12l-4.9 2.7 1.1-5.4-4-3.7 5.4-.6z"/><use href="#s" x="17"/><use href="#s" x="34"/><use href="#s" x="51"/><use href="#s" x="68"/></g></svg>
  </div>
  <div class="brand">Searchly</div>
  <h2 class="title">Positive: Professionalism,<br>Quality, Value</h2>
  <p class="body">The team did a good job of replacing a large feature window spanning two floors, as well as the others in my property. They're a professional group who were willing to work out solutions to any problem, especially compared to other companies. Prices are fair, and my new UPVC windows look great. Special thanks to Frank for being so accommodating and for the good communication throughout.</p>
  <p class="service">Service: Window installation</p>
  <p class="meta">11 months ago by Howard Pell</p>
</article>

<article class="card card-tp">
  <div class="badge-stars">
    <svg width="85" height="16" viewBox="0 0 85 16"><g fill="#f5c518"><use href="#s"/><use href="#s" x="17"/><use href="#s" x="34"/><use href="#s" x="51"/><use href="#s" x="68"/></g></svg>
  </div>
  <div class="brand"><span class="brand-mark"></span>TrustLane</div>
  <h2 class="title">Front door with windows each<br>side and side window</h2>
  <p class="body">This is the second time we have used meridian home Improvments , and the service is amazing! Daniel came round several times as we keep changing our minds and he was so helpful and gave us good advice, and the guys who do the fitting are efficient and tidy . I’ve got to say the end result is amazing and I have recommended to many of friends . Thanks Meridan</p>
  <p class="meta">13 Feb 2018 by Tom</p>
</article>

<article class="card card-yl">
  <div class="badge-stars">
    <svg width="85" height="16" viewBox="0 0 85 16"><g fill="#f5c518"><use href="#s"/><use href="#s" x="17"/><use href="#s" x="34"/><use href="#s" x="51"/><use href="#s" x="68"/></g></svg>
  </div>
  <div class="brand">Listra</div>
  <h2 class="title">Brilliant all round professional,<br>friendly service.</h2>
  <p class="body">This home run friendly business was a real pleasure to deal with. From the professional, no pressure quote, nothing was too much trouble to ensure everything is as required for your needs with the quote and fitting. The workmanship and double glazing being fitted was brilliant and my home/outdoors was left tidy and clean leaving an outstanding impression for such an all round professional job. I would not hesitate to recommend this company, such a brilliant service from great hardworking people that care about their service.</p>
  <p class="meta">13 Feb 2018 by GreenChair74</p>
</article>

<div class="load-more">LOAD MORE</div>

<div class="powered">
  <p class="powered-label">Powered by</p>
  <div class="powered-row">
    <span class="powered-mark"></span>
    <span class="powered-name">ReviewGather</span>
  </div>
</div>
</body>
</html>
```